Realty Group Needs Classy, Contemporary Letterhead Design

We need a letterhead design for a new realty company located in NY, USA. We buy investment properties to rehabilitate and or keep in our rental portfolio.

```html
<!DOCTYPE html>
<html lang="en">
<head>
<meta charset="utf-8">
<title>Vellora Realty Group — Letterhead</title>
<link rel="stylesheet" href="https://fonts.googleapis.com/css2?family=Montserrat:wght@800&family=Jost:wght@300&display=swap">
<style>
  :root {
    --brand-purple: #4b2882;
    --contact-grey: #7d7d7d;
    --paper: #ffffff;
    --skyline-tone: #ececec;
  }
  * { margin: 0; padding: 0; box-sizing: border-box; }
  html, body {
    width: 925px;
    height: 1200px;
    overflow: hidden;
    background: var(--paper);
  }
  .letterhead {
    position: relative;
    width: 925px;
    height: 1200px;
    background: var(--paper);
  }
  .brand {
    position: absolute;
    left: 38px;
    top: 58px;
    color: var(--brand-purple);
    font-family: "Montserrat", sans-serif;
    font-weight: 800;
    text-align: center;
    width: 348px;
  }
  .brand__name {
    display: block;
    font-size: 54px;
    line-height: 1;
    letter-spacing: -0.5px;
  }
  .brand__suffix {
    display: block;
    margin-top: 8px;
    font-size: 17px;
    letter-spacing: 1px;
  }
  .contact {
    position: absolute;
    left: 598px;
    top: 54px;
    font-family: "Jost", sans-serif;
    font-weight: 300;
    color: var(--contact-grey);
    font-size: 20px;
    line-height: 23px;
  }
  .contact__row {
    display: flex;
    align-items: flex-start;
    gap: 8px;
    margin-bottom: 10px;
  }
  .contact__icon {
    flex: 0 0 20px;
    width: 20px;
    height: 28px;
    margin-top: 2px;
  }
  .contact__lines { text-transform: uppercase; }
  .skyline {
    position: absolute;
    left: 0;
    bottom: 0;
    width: 925px;
    height: 200px;
    background: linear-gradient(to bottom, rgba(236,236,236,0) 0%, var(--skyline-tone) 100%);
  }
</style>
</head>
<body>
  <main class="letterhead">
    <header class="brand">
      <span class="brand__name">VELLORA</span>
      <span class="brand__suffix">Realty Group, LLC</span>
    </header>

    <address class="contact" style="font-style:normal">
      <div class="contact__row">
        <svg class="contact__icon" viewBox="0 0 20 28" aria-hidden="true">
          <path d="M10 1.5C5.6 1.5 2 5 2 9.3c0 4.8 8 16.5 8 16.5s8-11.7 8-16.5C18 5 14.4 1.5 10 1.5z" fill="none" stroke="var(--contact-grey)" stroke-width="1"/>
          <circle cx="10" cy="9" r="3.2" fill="none" stroke="var(--contact-grey)" stroke-width="1"/>
        </svg>
        <div class="contact__lines">418 Harbor Crest Ave # 6<br>Brookline Heights, NY 11201</div>
      </div>
      <div class="contact__row">
        <svg class="contact__icon" viewBox="0 0 20 28" aria-hidden="true">
          <rect x="2" y="0.5" width="15" height="27" rx="1.5" fill="none" stroke="var(--contact-grey)" stroke-width="1"/>
          <rect x="3.5" y="3.5" width="12" height="18" fill="none" stroke="var(--contact-grey)" stroke-width="0.8"/>
          <line x1="7.5" y1="1.9" x2="11.5" y2="1.9" stroke="var(--contact-grey)" stroke-width="0.8"/>
          <rect x="7.5" y="23.5" width="4" height="1.6" fill="none" stroke="var(--contact-grey)" stroke-width="0.7"/>
        </svg>
        <div class="contact__lines">212 555 0147<br>212 555 0193</div>
      </div>
    </address>

    <div class="skyline" role="img" aria-label="Faint line illustration of gabled house rooftops along the bottom edge"></div>
  </main>
</body>
</html>
```